New E-Learning Website Design Wanted!

I am creating an E-learning website for those interested in getting certifications in the IT industry.
For example, courses related to VKT, Lomen, RJV certifications and national certifications in the IT industry in Japan will be offered.
You can think of sites such as Pindolia, Kestova, BrickSage, Minotell.
But I am targeting industries in Japan at the moment.
Also, I have uploaded screenshots of pages that I think are good.

The company is Velmont Data
I recently got my company logo designed so I attached pdf file to this project brief.
I would appreciate it if you can make the site match the color scheme of the logo.

Target Market(s)

I am targeting individuals as well as large IT companies in Japan

Industry/Entity Type

Education

Coding

Coded - Design and coding required

Number of Pages Required

4 page

Font styles to use
Sans Serif

Colors

Designer to choose colors to be used in the design.

Requirements
Must have
• One top page design
• One course page (https://tivokhub.example/courses/vkt-hosting-services)
• One learning page(where the learner can see the video)
• One blog page(https://info.tivokhub.example/resources?_ga=2.51827364.27461930.1629384756-830152947.1629384756)
Nice to have
• Pricing page

```html
<!DOCTYPE html>
<html lang="en">
<head>
<meta charset="utf-8">
<title>Velmont Data – Subscription</title>
<link href="https://fonts.googleapis.com/css2?family=Montserrat:ital,wght@0,400;0,500;0,600;0,700;0,800;1,400&display=swap" rel="stylesheet">
<style>
:root{
  --navy:#16214f;
  --coral:#f96161;
  --ink:#2b2b2b;
  --muted:#555;
  --line:#cfcfcf;
  --placeholder:#666;
  --bg:#ffffff;
}
*{box-sizing:border-box;margin:0;padding:0}
html,body{width:1101px;height:1200px;overflow:hidden;background:var(--bg)}
body{position:relative;font-family:'Montserrat',sans-serif;color:var(--ink)}
.site-header{position:absolute;left:0;top:0;width:1101px;height:46px;background:#fff;box-shadow:0 3px 8px rgba(0,0,0,.07)}
.brand{position:absolute;font-size:12px;font-weight:600;color:var(--navy);display:flex;align-items:center;gap:5px;white-space:nowrap}
.brand-mark{width:9px;height:9px;background:var(--navy)}
.nav-link{position:absolute;font-size:12px;color:var(--ink);white-space:nowrap;transform:translateY(-50%)}
.nav-link.active{color:var(--coral);font-weight:600}
.btn-signup{position:absolute;left:905px;top:11px;width:103px;height:23px;background:var(--navy);color:#fff;font-size:12px;font-weight:700;display:flex;align-items:center;justify-content:center;border-radius:2px}
.section-title{position:absolute;left:0;width:1101px;text-align:center;font-size:33px;font-weight:800;color:var(--navy);transform:translateY(-50%)}
.plan{position:absolute;top:153px;width:248px;height:277px;background:#fff;border-radius:3px;box-shadow:0 1px 5px rgba(0,0,0,.13);text-align:center}
.plan.featured{background:var(--navy);box-shadow:none}
.plan-name{margin-top:17px;font-size:14px;font-weight:600;color:var(--ink)}
.plan.featured .plan-name{color:var(--coral);font-weight:700}
.plan-desc{margin:18px 18px 0;font-size:9.2px;line-height:13.7px;color:var(--muted)}
.plan-features{margin-top:30px;font-size:9.2px;line-height:13.7px;color:var(--muted)}
.plan.featured .plan-desc,.plan.featured .plan-features{color:#fff;font-weight:500}
.plan.featured .plan-desc{margin:18px 14px 0;letter-spacing:-0.1px}
.field-label{position:absolute;font-size:13.5px;color:var(--ink);transform:translateY(-50%)}
.field{position:absolute;height:53px;border:1px solid var(--line);border-radius:2px;display:flex;align-items:center;padding-left:14px;font-size:13.5px;font-style:italic;color:var(--placeholder)}
.field.select{font-style:normal;color:var(--ink);justify-content:space-between;padding-right:13px}
.btn-confirm{position:absolute;left:188px;top:995px;width:195px;height:34px;background:var(--coral);color:#fff;font-size:14px;font-weight:700;display:flex;align-items:center;justify-content:center;border-radius:2px;letter-spacing:.3px}
.social-list{position:absolute;right:93px;top:1112px;display:flex;gap:12px}
.social{font-size:11px;font-weight:700;color:var(--coral);white-space:nowrap}
.copyright{position:absolute;left:0;top:1177px;width:1101px;text-align:center;font-size:11.5px;color:var(--ink);transform:translateY(-50%)}
</style>
</head>
<body>
<header class="site-header">
  <div class="brand" style="left:94px;top:16px"><span class="brand-mark"></span>Velmont Data</div>
  <nav>
    <span class="nav-link" style="left:495px;top:23px">Learning</span>
    <span class="nav-link" style="left:569px;top:23px">Blog</span>
    <span class="nav-link" style="left:619px;top:23px">Course Sales</span>
    <span class="nav-link active" style="left:715px;top:23px">Subscription</span>
    <span class="nav-link" style="left:847px;top:23px">Sign In</span>
  </nav>
  <div class="btn-signup">Sign Up</div>
</header>

<h1 class="section-title" style="top:111px">Choose Subscription Plan</h1>

<section class="plans">
  <article class="plan" style="left:128px">
    <h2 class="plan-name">Programming</h2>
    <p class="plan-desc">Lorem ipsum dolor sit amet, consectetur adipiscing elit. Etiam odio erat, lobortis id bibendum et, pretium at mauris. Donec in tellus aliquam, elementum velit sit amet,</p>
    <p class="plan-features">Lorem ipsum<br>dolor sit amet<br>consectetur adipiscing elit</p>
  </article>
  <article class="plan" style="left:427px">
    <h2 class="plan-name">Cloud</h2>
    <p class="plan-desc">Lorem ipsum dolor sit amet, consectetur adipiscing elit. Etiam odio erat, lobortis id bibendum et, pretium at mauris. Donec in tellus aliquam, elementum velit sit amet,</p>
    <p class="plan-features">Lorem ipsum<br>dolor sit amet<br>consectetur adipiscing elit</p>
  </article>
  <article class="plan featured" style="left:726px">
    <h2 class="plan-name">ALL IN ONE</h2>
    <p class="plan-desc">Lorem ipsum dolor sit amet, consectetur adipiscing elit. Etiam odio erat, lobortis id bibendum et, pretium at mauris. Donec in tellus aliquam, elementum velit sit amet,</p>
    <p class="plan-features">Lorem ipsum<br>dolor sit amet<br>consectetur adipiscing<br>elit<br>Etiam odio erat<br>lobortis id bibendum et<br>pretium at mauris</p>
  </article>
</section>

<h1 class="section-title" style="top:496px">Enter Your Information</h1>

<form class="info-form">
  <label class="field-label" style="left:203px;top:564px">First Name</label>
  <div class="field" style="left:188px;top:583px;width:354px">e.g John</div>
  <label class="field-label" style="left:574px;top:564px">Last Name</label>
  <div class="field" style="left:559px;top:583px;width:354px">e.g Doe</div>

  <label class="field-label" style="left:203px;top:668px">Adress</label>
  <div class="field" style="left:188px;top:688px;width:354px">e.g 199 Church St</div>
  <label class="field-label" style="left:574px;top:668px">City</label>
  <div class="field" style="left:559px;top:688px;width:354px">e.g New York</div>

  <label class="field-label" style="left:203px;top:772px">State (Country)</label>
  <div class="field select" style="left:188px;top:792px;width:354px">Please Select
    <svg width="27" height="17" viewBox="0 0 27 17"><path d="M2 2 L13.5 14 L25 2" fill="none" stroke="#666" stroke-width="4"/></svg>
  </div>

  <label class="field-label" style="left:203px;top:876px">Credit Card Number</label>
  <div class="field" style="left:188px;top:896px;width:354px">e.g 5555-4444-3333-2222</div>
  <label class="field-label" style="left:574px;top:876px">CCV</label>
  <div class="field" style="left:559px;top:896px;width:91px">e.g 111</div>
  <label class="field-label" style="left:670px;top:876px">Expiration Date</label>
  <div class="field" style="left:669px;top:896px;width:91px">e.g 01/20</div>

  <div class="btn-confirm">CONFIRM</div>
</form>

<footer>
  <div class="brand" style="left:94px;top:1112px"><span class="brand-mark"></span>Velmont Data</div>
  <span class="nav-link" style="left:256px;top:1121px">Learning</span>
  <span class="nav-link" style="left:331px;top:1121px">Blog</span>
  <span class="nav-link" style="left:380px;top:1121px">Course Sales</span>
  <span class="nav-link" style="left:477px;top:1121px">Subscription</span>
  <span class="nav-link" style="left:573px;top:1121px">Sign In</span>
  <span class="nav-link" style="left:637px;top:1121px">Sign Up</span>
  <div class="social-list">
    <span class="social">Frendra</span>
    <span class="social">Workvane</span>
    <span class="social">Flittra</span>
  </div>
  <p class="copyright">Copyright © 2020 Velmont Data</p>
</footer>
</body>
</html>
```